**Business Card**Designs Project** LornaTrade,LLC

Im looking for a simple and elegant Business Card that has a professional Corporate look and feel. Im considering a Metal business card as well as 2 color layout, Embossed, 1 color two tone layout(File#6 like).

The card should NOT be too busy but subtle. Clean look providing Key Details.

please see uploaded files for actual logo and inspirational design i like.

See Uploaded File # 3 for Professional Logos Style

Target Market(s)

investors

Industry/Entity Type

Business

Contact Information for Business Card

Side 1 information
Lorna Trade,LLC - Description Text below main logo = (Funding - Sales) or (Commercial - Residential) or (Property - Funding )
www.lornatrade-demo.com

Side 2 Information =
Dov Pelkin | Managing Broker
P 555-014-7781 | F 555-016-2490
E info@lornatrade-demo.com
membership logos - see file #3 for stye and file #4 for inspiration

Side 2 = 10pt Font
BRE: 07281944
NMLS: 6620573

Colors
3277b5
5c5c5c
333333
959595
85acd3
1b1b1b
ffffff

Requirements
Must have
• Lorna Trade, LLC **G Logo** - See Uploaded File #5 ,
• Contact Information - See Business Card Details Above
• Web address = www.lornatrade-demo.com
• Membership logos - See Uploaded File #4 & 9
Nice to have
• 1 Color two tones, grey, White, Charcoal Grey, Dark Turquois, Dark blue, Slate blue,
• GOOD COMBINATIONS: White and Grey, white and Charcoal grey with a splash of blue, Charcoal grey card with White, etc..
• PLEASE TRY DARK BLUE DESIGNS
• Embossed, card designs
• Metal Business card design
Should not have
• I DONT LIKE ALOTE OF WAVE DESIGNS

```html
<!DOCTYPE html>
<html lang="en">
<head>
<meta charset="utf-8">
<title>Lorna Trade, LLC — Business Card</title>
<link rel="stylesheet" href="https://fonts.googleapis.com/css2?family=Montserrat:wght@400;500;600&display=swap">
<style>
  :root {
    --page: #e9eaec;
    --card: #ffffff;
    --blue: #2f86c0;
    --blue-deep: #3277b5;
    --swoosh: #5c5c5c;
    --ink: #333333;
    --muted: #959595;
    --white: #ffffff;
    --badge: #85acd3;
  }
  * { margin: 0; padding: 0; box-sizing: border-box; }
  html, body {
    width: 1200px; height: 899px; overflow: hidden;
    background: var(--page);
    font-family: "Montserrat", Arial, sans-serif;
  }
  .card {
    position: absolute; left: 150px; top: 192px;
    width: 900px; height: 514px;
    border-radius: 34px; overflow: hidden;
    background: var(--card);
    box-shadow: 0 14px 40px rgba(0,0,0,.18);
  }
  .card-shapes { position: absolute; inset: 0; }
  .brand {
    position: absolute; left: 70px; top: 110px; width: 320px;
    text-align: center;
  }
  .brand-mark {
    width: 78px; height: 78px; border-radius: 50%;
    border: 6px solid var(--blue-deep);
    margin: 0 auto 18px;
  }
  .brand-name {
    font-size: 31px; font-weight: 500; letter-spacing: 1px;
    color: var(--ink); line-height: 1.1;
  }
  .brand-tagline {
    margin-top: 6px; padding-top: 6px;
    border-top: 1px solid var(--muted);
    font-size: 12px; letter-spacing: 2px; color: var(--blue-deep);
  }
  .details { position: absolute; left: 540px; top: 62px; width: 330px; color: var(--white); }
  .person-name { font-size: 24px; font-weight: 500; letter-spacing: 1px; margin-left: 44px; }
  .person-role { font-size: 16px; margin-top: 4px; margin-left: 58px; }
  .address { font-size: 19px; line-height: 1.4; margin-top: 40px; margin-left: 44px; }
  .contacts { list-style: none; margin-top: 40px; }
  .contacts li {
    display: flex; align-items: center; gap: 12px;
    font-size: 15px; letter-spacing: .5px; height: 27px;
  }
  .contacts svg { width: 16px; height: 16px; fill: var(--white); flex: none; }
  .licenses {
    display: flex; align-items: center; gap: 10px;
    margin-top: 16px; font-size: 13px; letter-spacing: .5px;
  }
  .membership { display: flex; gap: 8px; margin-left: auto; }
  .membership-badge {
    width: 30px; height: 30px; border-radius: 50%;
    background: var(--badge); border: 2px solid var(--white);
  }
</style>
</head>
<body>
<main class="card">
  <svg class="card-shapes" viewBox="0 0 900 514" preserveAspectRatio="none" aria-hidden="true">
    <path d="M420 0 C560 70 545 310 330 420 C240 466 120 496 20 514 L900 514 L900 0 Z" fill="var(--swoosh)"/>
    <path d="M436 0 C572 72 560 312 350 424 C262 470 140 500 50 514 L900 514 L900 0 Z" fill="var(--card)"/>
    <path d="M446 0 C582 74 572 314 362 428 C276 474 156 503 70 514 L900 514 L900 0 Z" fill="var(--blue)"/>
  </svg>

  <section class="brand">
    <div class="brand-mark"></div>
    <p class="brand-name">LORNA TRADE<br>LLC</p>
    <p class="brand-tagline">COMMERCIAL &amp; RESIDENTIAL</p>
  </section>

  <section class="details">
    <p class="person-name">DOV PELKIN</p>
    <p class="person-role">Managing Broker</p>
    <p class="address">214,9th floor,Harbor<br>Ridge Road LKV</p>
    <ul class="contacts">
      <li><svg viewBox="0 0 16 16"><path d="M3 1l3 3-2 2c1 2 3 4 5 5l2-2 3 3-2 3C7 15 1 9 1 3z"/></svg>P 555-014-7781</li>
      <li><svg viewBox="0 0 16 16"><path d="M1 5h14v8H1zM4 2h8v3H4zm0 8h8v4H4z"/></svg>F 555-016-2490</li>
      <li><svg viewBox="0 0 16 16"><path d="M1 3h14v10H1zm1 1l6 5 6-5z"/></svg>info@lornatrade-demo.com</li>
      <li><svg viewBox="0 0 16 16"><path d="M8 0a8 8 0 100 16A8 8 0 008 0zm0 2c1 1 2 3 2 6s-1 5-2 6c-1-1-2-3-2-6s1-5 2-6zM2 7h12v2H2z"/></svg>www.lornatrade-demo.com</li>
    </ul>
    <div class="licenses">
      <span>BRE: 07281944 &nbsp;|&nbsp; NMLS: 6620573</span>
      <div class="membership" role="img" aria-label="Membership badges">
        <span class="membership-badge"></span>
        <span class="membership-badge"></span>
      </div>
    </div>
  </section>
</main>
</body>
</html>
```